Business Card Design

We are a state licensed general contractor on the south east coast of Florida. We are a remodeling and home repairs business that have been in business for 14 years. Since we are located on the coast and our business name is Ridgeline Builders of Pine Hollow, Inc, we would like a "Ridgeline" themed design that would appeal to more affluent customers. I would like to see light blue colors with waves incorporated into the design. I would also like the design to communicate a modern, confident, responsible company character.

Industry/Entity Type

Contractor

Contact Information for Business Card

Tim Wexler 555-274-9183

```html
<!DOCTYPE html>
<html lang="en">
<head>
<meta charset="utf-8">
<title>Ridgeline Builders – Business Card</title>
<link rel="stylesheet" href="https://fonts.googleapis.com/css2?family=Montserrat:wght@400;500;700;800&display=swap">
<style>
  :root {
    --bg: #e4e4e6;
    --card-top: #2f68b0;
    --card-mid: #2b5a9c;
    --card-bottom: #2a4f8a;
    --white: #ffffff;
    --accent: #4fb3ea;
  }
  * { margin: 0; padding: 0; box-sizing: border-box; }
  html, body {
    width: 1200px; height: 900px; overflow: hidden;
    background: var(--bg);
    font-family: "Montserrat", Arial, sans-serif;
  }
  .card {
    position: absolute;
    left: 110px; top: 170px;
    width: 980px; height: 560px;
    background: linear-gradient(175deg, var(--card-top) 0%, var(--card-mid) 55%, var(--card-bottom) 100%);
    overflow: hidden;
    box-shadow: 0 14px 30px rgba(0,0,0,0.18);
    color: var(--white);
  }
  .card__wave { position: absolute; inset: 0; width: 100%; height: 100%; }
  .brand {
    position: absolute; right: 130px; top: 36px;
    font-size: 44px; font-weight: 700; letter-spacing: 0.5px; line-height: 1.2;
    display: flex; align-items: center; gap: 14px;
  }
  .brand__dot {
    width: 16px; height: 16px; border-radius: 50%;
    background: var(--white);
  }
  .person__name {
    position: absolute; left: 120px; top: 150px;
    font-size: 52px; font-weight: 800; letter-spacing: 2px; line-height: 1;
  }
  .person__role {
    position: absolute; left: 250px; top: 286px;
    font-size: 22px; font-weight: 700; letter-spacing: 12px; line-height: 1;
  }
  .contact {
    position: absolute; right: 80px; top: 258px;
    text-align: right; font-size: 25px; font-weight: 500; line-height: 1.32;
    font-style: normal;
  }
  .contact__label { color: var(--accent); }
</style>
</head>
<body>
  <section class="card">
    <svg class="card__wave" viewBox="0 0 980 560" preserveAspectRatio="none" aria-hidden="true">
      <defs>
        <linearGradient id="swoosh" x1="0" y1="0" x2="1" y2="0">
          <stop offset="0" stop-color="#9fb3cf" stop-opacity="0.4"/>
          <stop offset="0.45" stop-color="#ffffff"/>
          <stop offset="1" stop-color="#e8ecf2"/>
        </linearGradient>
        <linearGradient id="lowerGlow" x1="0" y1="0" x2="0" y2="1">
          <stop offset="0" stop-color="#3570bb" stop-opacity="0.55"/>
          <stop offset="1" stop-color="#2a4f8a" stop-opacity="0"/>
        </linearGradient>
      </defs>
      <path d="M0,282 C300,268 600,245 770,172 C870,130 935,85 955,30 L980,30 L980,560 L0,560 Z" fill="url(#lowerGlow)"/>
      <path d="M0,270 C300,250 600,220 760,150 C860,105 925,75 955,30 C935,85 870,130 770,172 C600,245 300,268 0,282 Z" fill="url(#swoosh)"/>
    </svg>

    <div class="brand"><span class="brand__dot"></span>Ridgeline</div>

    <h1 class="person__name">TIM WEXLER</h1>
    <p class="person__role">OWNER</p>

    <address class="contact">
      4280 Harlan Circle Pine Hollow,<br>
      FL 34910<br>
      <span class="contact__label">Cell</span> 555 - 274.9183<br>
      <span class="contact__label">Office</span> 555 - 318.6620<br>
      ridgeline.tw@example.com
    </address>
  </section>
</body>
</html>
```